Glenvora pond linings website template

We need a template for our new website. Glenvora is currently marketed through www.sheetvale.com.au, and we are moving the pond/dam linings to a dedicated site www.glenvora.com.au

The site is essentially brochureware. The content (less landing page & photo gallery) is on the new site to give you a better idea of what we do. We are also on Facebook.com/glenvora

We are looking for a template/style which we can adapt to the different sections of the site as required. We also get a lot of phone/tablet visitors so an alternative mobile layout would be a bonus, but by no means required.

I am proficient in HTML/CSS & javascript so can code most designs thrown at me.

Any icons or interface fonts should be freely available web fonts where possible.

Target Market(s)

We are targeting both landscape professionals (design & construction) as well as the DIY market for ponds/wateragrdens.

Industry/Entity Type

Moving

Requirements
Must have
• We need a design (preferably layered PSD or AI) as basis for our overall site look and feel. Fonts/iconography/layout are where we are lacking. We can do the HTML/CSS/JS/PHP internally.
Nice to have
• A style guide either in file or separate would be nice.
Layers with effect (i.e.. :hover, CSS3 transition endpoints, etc)

```html
<!DOCTYPE html>
<html lang="en">
<head>
<meta charset="utf-8">
<title>Glenvora – Custom made liners for ponds, pools &amp; watergardens</title>
<link href="https://fonts.googleapis.com/css2?family=Arimo:wght@400;700&family=Kaushan+Script&display=swap" rel="stylesheet">
<style>
:root{
  --lime:#c6db3c;
  --lime-dark:#6f9a1e;
  --leaf:#5f9322;
  --navy:#1d3f72;
  --teal:#1a7a5a;
  --grey:#9a9a9a;
  --text:#555;
  --panel:#eef6cf;
  --rule:#e4e4e4;
  --white:#fff;
}
*{box-sizing:border-box;margin:0;padding:0}
html,body{width:1200px;height:800px;overflow:hidden}
body{
  position:relative;
  font-family:Arimo,Arial,sans-serif;
  background:radial-gradient(ellipse at 50% 10%,#dff0a8 0%,#a9d24a 45%,#4f8d16 100%);
}
.band{position:absolute;left:0;top:80px;width:1200px;height:53px;background:var(--lime)}
.page{
  position:absolute;left:119px;top:23px;width:950px;height:768px;
  background:var(--white);border:6px solid var(--lime-dark);border-radius:14px;
}
.search{
  position:absolute;left:662px;top:12px;width:268px;height:34px;
  border:1px solid #e2e2e2;border-radius:10px;
  font-size:10px;color:#ccc;padding:11px 14px;
}
.search svg{position:absolute;right:14px;top:7px}
.brand{position:absolute;left:15px;top:56px;width:220px}
.brand-name{display:flex;align-items:center;gap:10px;height:90px;border-bottom:0}
.brand-mark{width:34px;height:34px;background:var(--leaf)}
.brand-word{font-size:34px;font-weight:400;color:var(--teal);letter-spacing:2px}
.brand-tag{font-size:9px;color:var(--teal);margin-top:6px}
.nav{
  position:absolute;left:241px;top:57px;width:688px;height:54px;background:var(--lime);
  display:flex;align-items:center;padding-left:34px;gap:0;
}
.nav a{font-size:10px;font-weight:700;color:var(--navy);text-decoration:none;margin-right:26px;position:relative}
.nav a.current::after{content:"";position:absolute;left:50%;top:30px;margin-left:-7px;border:7px solid transparent;border-bottom-color:var(--white)}
.hero{
  position:absolute;left:241px;top:121px;width:688px;height:276px;
  border:2px solid var(--rule);padding:2px;
}
.hero div{width:100%;height:100%;background:linear-gradient(120deg,#5f6b7a 0%,#7b6a55 35%,#4e6b2e 60%,#b08560 100%)}
.side{position:absolute;left:15px;width:216px}
.side h3{font-size:12px;font-weight:400;color:var(--navy);padding:14px 0;border-top:1px solid var(--rule);border-bottom:1px solid var(--rule)}
.products{top:212px}
.products ul{list-style:none;margin-top:14px;font-size:12px;color:var(--grey);line-height:15px}
.news{top:401px}
.news time{display:block;font-size:9px;color:var(--navy);margin:16px 0 19px}
.news p{font-size:10px;color:var(--text);line-height:15px}
.profile{
  position:absolute;left:241px;top:402px;width:688px;height:216px;background:var(--panel);
  padding:10px 12px;
}
.profile h2{font-size:15px;font-weight:400;color:var(--navy);margin-bottom:10px}
.profile p{width:366px;font-size:9.5px;line-height:15px;color:var(--text);margin-bottom:15px}
.profile-photo{
  position:absolute;left:381px;top:41px;width:302px;height:164px;background:var(--white);padding:3px;
}
.profile-photo div{width:100%;height:100%;background:linear-gradient(180deg,#8c7b62 0%,#6f6f66 45%,#3d4d48 100%)}
.footer-rule{position:absolute;left:15px;right:0;top:670px;border-top:1px solid #eee}
.follow{
  position:absolute;left:29px;top:657px;width:153px;height:40px;background:var(--lime);
  font-family:"Kaushan Script",cursive;color:var(--white);font-size:20px;text-align:center;line-height:40px;
}
.follow::before{content:"";position:absolute;left:-14px;top:0;border:7px solid transparent;border-right-color:var(--lime-dark);border-top-color:var(--lime-dark)}
.social{position:absolute;left:55px;top:709px;display:flex;gap:10px}
.social span{width:20px;height:20px;border:1px solid #ccc;border-radius:2px;background:linear-gradient(#fff,#eee)}
.copyright{position:absolute;left:240px;top:696px;font-size:9px;color:var(--grey)}
</style>
</head>
<body>
<div class="band"></div>
<div class="page">
  <div class="search">Search
    <svg width="18" height="18" viewBox="0 0 18 18"><circle cx="7" cy="7" r="5.5" fill="none" stroke="#aaa" stroke-width="2"/><line x1="11" y1="11" x2="16.5" y2="16.5" stroke="#aaa" stroke-width="2.5" stroke-linecap="round"/></svg>
  </div>
  <div class="brand">
    <div class="brand-name"><span class="brand-mark"></span><span class="brand-word">Glenvora</span></div>
    <p class="brand-tag">Custom made liners for ponds, pools &amp; watergardens.</p>
  </div>
  <nav class="nav">
    <a class="current">HOME</a><a>ABOUT US</a><a>HAPPENINGS</a><a>GALLERY</a><a>LINER STYLES</a><a>PREPARATION</a><a>INSTALLATION</a><a>CONTACT US</a>
  </nav>
  <div class="hero"><div role="img" aria-label="Shop window display planted with flowers and driftwood beside a brick street"></div></div>
  <section class="side products">
    <h3>HEADING</h3>
    <ul>
      <li>SVM 163 Penetrative Sealer</li><li>Roof &amp; Gutter Silicone</li><li>Primara</li>
      <li>Aquabond 501 (SVM 501)</li><li>Aquabond 300 (SVM 300)</li>
      <li>Coverlock Self Stick (SVM 3000X)</li><li>Flexacoat Premixed (SVM 001)</li>
    </ul>
  </section>
  <section class="side news">
    <h3>NEWS</h3>
    <time>20/08/2013</time>
    <p>Glenvora pond liners put an end to the compli-cated and time consuming installation used by other methods.</p>
    <time>20/08/2013</time>
    <p>Glenvora pond liners put an end to the compli-cated and time consuming installation used by other methods.</p>
  </section>
  <section class="profile">
    <h2>Company Profile</h2>
    <p>Glenvora has been manufactured, marketed and installed throughout Australia and the Pacific Rim since the early 1980's for a variety of domestic and commercial applications.</p>
    <p>Glenvora pond liners put an end to the complicated and time consuming installation used by other methods. Simply excavate or construct the desired shape of your pond pool or water garden, indoor or outdoor, place your Glenvora into position and secure the edges. It can easily be completed in a weekend. Glenvora pond liners are long lasting, economical to install and completely maintenance free.</p>
    <div class="profile-photo"><div role="img" aria-label="Garden pond with rocks, a small waterfall and reeds by a timber fence"></div></div>
  </section>
  <div class="footer-rule"></div>
  <div class="follow">Follow Us</div>
  <div class="social"><span></span><span></span><span></span><span></span></div>
  <p class="copyright">Glenvora Copyright. All Right Reserved 2013.</p>
</div>
</body>
</html>
```